Institute for Hollow Relief at Annapolis
business card and stationary
Institute for Hollow Relief at Annapolis -
Creative Brief
Professional
Dominic T. Halloway, MD
472 Fenwick Court, Suite 208 Annapolis, MD 21409
dthalloway82@mailbright.example
www.wombrelief.example
Use new logo Comprehensive Gynecologic Care with Specialization in Chronic Pain Disorders and Minimally Invasive Surgery
Appointment Date and Time: Mon. _______ Tue _____ Wed ______ Thurs_______ Fri_______ _______ AM _______ PM

```html
<!DOCTYPE html>
<html lang="en">
<head>
<meta charset="utf-8">
<title>Institute for Hollow Relief at Annapolis — Stationery</title>
<link rel="stylesheet" href="https://fonts.googleapis.com/css2?family=Open+Sans:wght@400;600;700&display=swap">
<style>
:root{
  --backdrop:#ecebe7;
  --paper:#ffffff;
  --brand-green:#3f9d4a;
  --brand-teal:#2a9a8a;
  --light-green:#a9d46f;
  --ink:#333333;
  --muted:#8a8a8a;
  --rule:#c9c9c9;
  --flap:#1b1b1b;
}
*{box-sizing:border-box;margin:0;padding:0}
html,body{width:1200px;height:454px;overflow:hidden}
body{background:var(--backdrop);font-family:"Open Sans",Arial,sans-serif;color:var(--ink);position:relative}
.sheet,.envelope,.card{position:absolute;background:var(--paper);box-shadow:0 2px 6px rgba(0,0,0,.18);overflow:hidden}
.sheet{top:50px;width:240px;height:310px}
.sheet--one{left:29px}
.sheet--two{left:300px}
.sheet--three{left:566px}
.brand{position:absolute;display:flex;align-items:center;gap:4px}
.brand__dot{width:12px;height:12px;border-radius:50%;background:var(--brand-green);flex:none}
.brand__name{font-weight:700;color:var(--brand-green);font-size:6px;line-height:1.15;text-transform:uppercase;width:62px}
.sheet .brand{top:14px;left:50%;transform:translateX(-50%)}
.sheet--two .brand{left:82px;transform:none}
.contact{position:absolute;font-size:3.4px;line-height:1.4;color:var(--muted)}
.sheet--two .contact{top:16px;left:162px}
.sheet--one .contact{bottom:10px;left:0;right:0;text-align:center}
.watermark{position:absolute;left:-40px;top:110px;width:150px;height:150px;border-radius:50%;background:var(--brand-green);opacity:.07}
.swoosh{position:absolute;left:0;bottom:0;width:100%;height:60px}
.fax-title{position:absolute;top:66px;left:16px;font-size:15px;font-weight:700}
.fax-fields{position:absolute;top:66px;left:92px;width:134px;font-size:4px;color:var(--muted)}
.fax-fields div{border-bottom:1px solid var(--rule);height:10px;padding-top:3px}
.fax-checks{position:absolute;top:146px;left:16px;right:14px;display:flex;justify-content:space-between;font-size:3.6px;color:var(--muted)}
.fax-checks span::before{content:"";display:inline-block;width:4px;height:4px;border:.5px solid var(--muted);margin-right:2px;vertical-align:middle}
.fax-rule{position:absolute;top:140px;left:16px;right:14px;border-top:1px solid var(--rule)}
.envelope{width:336px;height:86px;left:840px}
.envelope--back{top:58px}
.envelope--front{top:122px;height:110px}
.envelope__flap{position:absolute;inset:0}
.envelope--front .brand{top:12px;left:12px}
.envelope--front .contact{bottom:28px;left:12px}
.card{width:96px;height:55px;top:372px}
.card--front{left:876px}
.card--back{left:989px}
.card .brand{top:6px;left:6px;gap:2px}
.card .brand__dot{width:7px;height:7px}
.card .brand__name{font-size:3.4px;width:40px}
.card .person{position:absolute;top:22px;left:6px;font-size:3.4px;line-height:1.4;color:var(--muted)}
.card .person b{color:var(--ink)}
.card .swoosh{height:18px}
.appointment{position:absolute;top:6px;left:6px;right:6px;font-size:3.3px;line-height:1.6;color:var(--muted)}
.appointment b{color:var(--brand-green);display:block}
.option-label{position:absolute;top:428px;font-size:11px;color:#555}
</style>
</head>
<body>

<section class="sheet sheet--one" aria-label="Letterhead option 1">
  <div class="watermark"></div>
  <div class="brand"><span class="brand__dot"></span><span class="brand__name">Institute for Hollow Relief at Annapolis</span></div>
  <p class="contact">472 Fenwick Court, Suite 208 Annapolis, MD 21409 · dthalloway82@mailbright.example · www.wombrelief.example</p>
</section>

<section class="sheet sheet--two" aria-label="Letterhead option 2">
  <div class="brand"><span class="brand__dot"></span><span class="brand__name">Institute for Hollow Relief at Annapolis</span></div>
  <p class="contact">Dominic T. Halloway, MD<br>472 Fenwick Court, Suite 208<br>Annapolis, MD 21409<br>dthalloway82@mailbright.example<br>www.wombrelief.example</p>
  <svg class="swoosh" viewBox="0 0 240 60" preserveAspectRatio="none">
    <path d="M0 46 Q120 60 240 14" fill="none" stroke="var(--light-green)" stroke-width="2"/>
    <path d="M0 52 Q130 62 240 24 L240 60 L0 60Z" fill="var(--brand-teal)" opacity=".9"/>
  </svg>
</section>

<section class="sheet sheet--three" aria-label="Fax cover sheet">
  <div class="brand"><span class="brand__dot"></span><span class="brand__name">Institute for Hollow Relief at Annapolis</span></div>
  <h1 class="fax-title">FAX</h1>
  <div class="fax-fields">
    <div>To:</div><div>From:</div><div>Fax:</div><div>Phone:</div><div>Date:</div><div>Re:</div>
  </div>
  <div class="fax-rule"></div>
  <div class="fax-checks"><span>Urgent</span><span>For Review</span><span>Please Comment</span><span>Please Reply</span><span>Please Recycle</span></div>
  <svg class="swoosh" viewBox="0 0 240 60" preserveAspectRatio="none">
    <path d="M0 46 Q120 60 240 14" fill="none" stroke="var(--light-green)" stroke-width="2"/>
    <path d="M0 52 Q130 62 240 24 L240 60 L0 60Z" fill="var(--brand-teal)" opacity=".9"/>
  </svg>
</section>

<section class="envelope envelope--back" aria-label="Envelope back">
  <svg class="envelope__flap" viewBox="0 0 336 86" preserveAspectRatio="none">
    <path d="M0 0 H336 L190 52 Q168 60 146 52 Z" fill="var(--flap)"/>
    <circle cx="168" cy="34" r="7" fill="var(--brand-green)"/>
  </svg>
</section>

<section class="envelope envelope--front" aria-label="Envelope front">
  <div class="brand"><span class="brand__dot"></span><span class="brand__name">Institute for Hollow Relief at Annapolis</span></div>
  <p class="contact">472 Fenwick Court, Suite 208 Annapolis, MD 21409</p>
  <svg class="swoosh" viewBox="0 0 336 30" preserveAspectRatio="none" style="height:30px">
    <path d="M0 22 Q180 34 336 4" fill="none" stroke="var(--light-green)" stroke-width="2"/>
    <path d="M0 26 Q190 36 336 10 L336 30 L0 30Z" fill="var(--brand-teal)"/>
  </svg>
</section>

<section class="card card--front" aria-label="Business card front">
  <div class="brand"><span class="brand__dot"></span><span class="brand__name">Institute for Hollow Relief at Annapolis</span></div>
  <p class="person"><b>Dominic T. Halloway, MD</b><br>472 Fenwick Court, Suite 208<br>dthalloway82@mailbright.example</p>
  <svg class="swoosh" viewBox="0 0 96 18" preserveAspectRatio="none">
    <path d="M0 14 Q50 20 96 2 L96 18 L0 18Z" fill="var(--brand-teal)"/>
  </svg>
</section>

<section class="card card--back" aria-label="Appointment card">
  <p class="appointment"><b>Appointment Date and Time:</b>Mon. ____ Tue ____ Wed ____<br>Thurs ____ Fri ____<br>____ AM ____ PM</p>
  <svg class="swoosh" viewBox="0 0 96 18" preserveAspectRatio="none">
    <path d="M0 14 Q50 20 96 2 L96 18 L0 18Z" fill="var(--brand-teal)"/>
  </svg>
</section>

<span class="option-label" style="left:122px">Option-1</span>
<span class="option-label" style="left:398px">Option-2</span>
<span class="option-label" style="left:662px">Option-3</span>

</body>
</html>
```